Business Card Design for company

We want new business cards. We'd like something different-- yet still highly professional. Our tagline is Providing leadership, delivering success. Stock photos are ok, as long as they are relevant and look upscale.

Target Market(s)

Architecture/Business Management Consulting/Engineering Consulting

Contact Information for Business Card

dark gray background with pops of blue might be good, but you tell me. You're the designers. Rounded corners might be nice, but again, you tell me.

Font styles to use
Serif
Sans Serif

Colors
3276b5
5c5c5c
9d9d9d
fbfbfb

Requirements
Nice to have
• Something different, but still very professional.

```html
<!DOCTYPE html>
<html lang="en">
<head>
<meta charset="utf-8">
<title>Norvale Business Card</title>
<link rel="stylesheet" href="https://fonts.googleapis.com/css2?family=Montserrat:wght@700&family=Roboto:wght@400;500;700&display=swap">
<style>
  :root {
    --backdrop: #1f2b33;
    --blue: #2f7de1;
    --card-gray: #9aa5a3;
    --band-dark: #495053;
    --ink: #4a5055;
    --white: #ffffff;
  }
  * { box-sizing: border-box; margin: 0; padding: 0; }
  html, body { width: 1200px; height: 1200px; overflow: hidden; }
  body { background: var(--backdrop); position: relative; font-family: "Roboto", Arial, sans-serif; }

  .card { position: absolute; left: 308px; width: 584px; overflow: hidden; }

  /* Front */
  .card-front { top: 135px; height: 382px; border-radius: 56px 40px 40px 56px; background: var(--card-gray); }
  .front-panel { position: absolute; left: 0; top: 0; width: 292px; height: 100%; background: var(--white); }
  .brand-name {
    font-family: "Montserrat", Arial, sans-serif; font-weight: 700; color: var(--blue);
    letter-spacing: 1px; text-align: center; line-height: 1;
  }
  .front-panel .brand-name { position: absolute; left: 0; width: 292px; top: 66px; font-size: 34px; }
  .tagline { position: absolute; left: 0; width: 292px; top: 169px; text-align: center; font-size: 11px; font-weight: 700; color: var(--ink); }
  .accent-bar { position: absolute; left: 61px; top: 206px; width: 176px; height: 17px; background: var(--blue); }
  .person-name { position: absolute; left: 0; width: 292px; top: 281px; text-align: center; font-size: 24px; font-weight: 500; color: var(--ink); }
  .person-title { position: absolute; left: 0; width: 292px; top: 311px; text-align: center; font-size: 6px; font-weight: 500; color: var(--ink); letter-spacing: 0.2px; }

  .contact-icon {
    position: absolute; left: 277px; width: 36px; height: 36px; border-radius: 50%;
    background: var(--white); display: flex; align-items: center; justify-content: center;
  }
  .contact-icon svg { width: 20px; height: 20px; }
  .contact-block { position: absolute; left: 343px; font-size: 11px; line-height: 12.5px; color: var(--white); }

  /* Back */
  .card-back { top: 588px; height: 381px; border-radius: 40px; background: var(--card-gray); }
  .stripe { position: absolute; height: 11px; }
  .stripe-left-top { left: 0; width: 198px; top: 170px; background: var(--blue); }
  .stripe-left-bottom { left: 0; width: 198px; top: 188px; background: var(--band-dark); }
  .stripe-right-top { left: 386px; right: 0; top: 170px; background: var(--band-dark); }
  .stripe-right-bottom { left: 386px; right: 0; top: 188px; background: var(--blue); }
  .card-back .brand-name { position: absolute; left: 198px; width: 188px; top: 163px; font-size: 34px; }
  .web-band {
    position: absolute; left: 0; right: 0; bottom: 0; height: 69px; background: var(--band-dark);
    display: flex; align-items: center; justify-content: center;
    color: var(--white); font-size: 14px; letter-spacing: 5px;
  }
</style>
</head>
<body>

<section class="card card-front">
  <div class="front-panel">
    <div class="brand-name">NORVALE</div>
    <p class="tagline">Providing leadership, delivering success</p>
    <div class="accent-bar"></div>
    <p class="person-name">Daniel Hart</p>
    <p class="person-title">DIRECTOR OF CONSULTING SERVICES</p>
  </div>

  <div class="contact-icon" style="top:118px">
    <svg viewBox="0 0 24 24"><path fill="#2f7de1" d="M12 2a7 7 0 0 0-7 7c0 5 7 13 7 13s7-8 7-13a7 7 0 0 0-7-7zm0 9.5A2.5 2.5 0 1 1 12 6.5a2.5 2.5 0 0 1 0 5z"/></svg>
  </div>
  <div class="contact-icon" style="top:154px">
    <svg viewBox="0 0 24 24" fill="none" stroke="#2f7de1" stroke-width="2"><circle cx="12" cy="12" r="9"/><path d="M3 12h18M12 3c3 3 3 15 0 18M12 3c-3 3-3 15 0 18"/></svg>
  </div>
  <div class="contact-icon" style="top:191px">
    <svg viewBox="0 0 24 24"><rect x="5" y="3" width="14" height="18" rx="1.5" fill="#2f7de1"/><path d="M8 8h8M8 11h8M8 14h8M8 17h6" stroke="#fff" stroke-width="1.4"/></svg>
  </div>
  <div class="contact-icon" style="top:228px">
    <svg viewBox="0 0 24 24"><path fill="#2f7de1" d="M6.6 10.8a15.1 15.1 0 0 0 6.6 6.6l2.2-2.2a1 1 0 0 1 1-.25 11.4 11.4 0 0 0 3.6.57 1 1 0 0 1 1 1V20a1 1 0 0 1-1 1A17 17 0 0 1 3 4a1 1 0 0 1 1-1h3.5a1 1 0 0 1 1 1c0 1.25.2 2.45.57 3.57a1 1 0 0 1-.25 1z"/></svg>
  </div>

  <div class="contact-block" style="top:117px">HEADQUARTERS<br>1450 Harbor Crest Way<br>Tampa, FL 33602</div>
  <div class="contact-block" style="top:166px">MEDIA AND PUBLIC RELATIONS<br>MEDIA@NORVALEINTL.COM</div>
  <div class="contact-block" style="top:206px">GENERAL INQUIRIES<br>INFO@NORVALEINTL.COM</div>
  <div class="contact-block" style="top:255px">1 (888) 555-0142</div>
</section>

<section class="card card-back">
  <div class="stripe stripe-left-top"></div>
  <div class="stripe stripe-left-bottom"></div>
  <div class="stripe stripe-right-top"></div>
  <div class="stripe stripe-right-bottom"></div>
  <div class="brand-name">NORVALE</div>
  <div class="web-band">www.norvaleintl.com</div>
</section>

</body>
</html>
```